Business Card Design for Consulting Company

I require a Business Card design for my Consulting company. <br/><br/>My company name is: Marek Olvani Consulting Inc.<br/>My website is: www.marekolvaniconsulting.example<br/><br/>My company focuses on management and software development for the Tallobrix CRM platform (www.tallobrix.example)<br/><br/>I have a logo already designed...see attached.
Updates

Also Include my Name and Title: Marek T.L. Olvani President

Target Market(s)

Tallobrix Customers

Contact Information for Business Card

Only include my LOGO (provided)
My Name: Marek TL Olvani
My Title: President
My Company Name: Marek Olvani Consulting Inc.
My Website: www.marekolvaniconsulting.example
My Email: marek.olvani.consulting@mailbox.example

NO PHONE NUMBER
NO ADDRESS

Font styles to use
Serif
Sans Serif
Other font styles liked:
• see my website: www.marekolvaniconsulting.example

Colors

Designer to choose colors to be used in the design.

Requirements
Must have
• Must include my Orange
• Include my name (Marek T.L. Olvani), title (President) company name, website and email
• It should also have a tag line like: Tallobrix Consulting
• I'm flexible with the tag line
Should not have
• Don't include my phone number or address

```html
<!DOCTYPE html>
<html lang="en">
<head>
<meta charset="utf-8">
<title>Marek Olvani Consulting Inc. — Business Card</title>
<link rel="stylesheet" href="https://fonts.googleapis.com/css2?family=Montserrat:wght@700&family=Roboto+Condensed:wght@400;500&family=Roboto:wght@400&display=swap">
<style>
  :root {
    --brand-orange: #f5821f;
    --brand-navy: #1f5478;
    --paper: #ffffff;
    --backdrop: #2a2a2a;
  }
  * { box-sizing: border-box; margin: 0; padding: 0; }
  html, body { width: 1200px; height: 900px; overflow: hidden; background: var(--backdrop); }
  .canvas { position: relative; width: 1200px; height: 900px; }

  .card {
    position: absolute; left: 250px; width: 700px; height: 400px; overflow: hidden;
  }
  .card-front { top: 36px; background: var(--brand-orange); }
  .card-back { top: 466px; background: var(--paper); }

  .brand {
    position: absolute; display: flex; align-items: center; gap: 14px;
    font-family: "Roboto Condensed", sans-serif; font-weight: 500;
    text-transform: uppercase; letter-spacing: 0.5px; line-height: 1.05;
  }
  .brand-square { width: 46px; height: 46px; border-radius: 6px; flex: none; }
  .brand-name { font-size: 28px; }

  .card-front .brand { left: 0; right: 0; top: 120px; justify-content: center; color: var(--paper); }
  .card-front .brand-square { background: var(--paper); }

  .front-rule {
    position: absolute; left: 0; right: 0; top: 285px; height: 1px; background: rgba(255,255,255,0.8);
  }
  .tagline {
    position: absolute; left: 0; right: 0; top: 322px; text-align: center;
    font-family: "Roboto Condensed", sans-serif; font-size: 14px;
    letter-spacing: 3px; text-transform: uppercase; color: var(--paper);
  }

  .card-back .brand { left: 40px; top: 40px; color: var(--brand-orange); }
  .card-back .brand-square { background: var(--brand-orange); }

  .wave { position: absolute; left: 0; top: 0; width: 700px; height: 400px; }
  .wave-band { fill: var(--brand-navy); }
  .wave-swoosh { fill: var(--brand-orange); }

  .contact {
    position: absolute; right: 40px; bottom: 22px; text-align: right; color: var(--paper);
    font-family: "Roboto", sans-serif;
  }
  .person-name {
    font-family: "Montserrat", sans-serif; font-weight: 700; font-size: 30px;
    color: var(--brand-orange); line-height: 1.1;
  }
  .person-title { font-size: 17px; line-height: 1.2; margin-bottom: 8px; font-family: "Roboto Condensed", sans-serif; }
  .contact-line {
    display: flex; justify-content: flex-end; align-items: center; gap: 10px;
    font-size: 17px; line-height: 1.5; font-family: "Roboto Condensed", sans-serif;
  }
  .contact-icon { width: 18px; height: 18px; flex: none; }
  .contact-icon * { fill: none; stroke: var(--brand-orange); stroke-width: 1.6; }
</style>
</head>
<body>
<main class="canvas">

  <section class="card card-front" aria-label="Card front">
    <div class="brand">
      <span class="brand-square"></span>
      <span class="brand-name">Marek Olvani<br>Consulting Inc.</span>
    </div>
    <div class="front-rule"></div>
    <p class="tagline">Tallobrix Consulting</p>
  </section>

  <section class="card card-back" aria-label="Card back">
    <div class="brand">
      <span class="brand-square"></span>
      <span class="brand-name">Marek Olvani<br>Consulting Inc.</span>
    </div>

    <svg class="wave" viewBox="0 0 700 400" aria-hidden="true">
      <path class="wave-swoosh" d="M10 205 C 60 245, 200 262, 340 250 C 440 241, 500 216, 560 217 C 500 224, 440 252, 340 262 C 200 276, 60 262, 4 224 Z"/>
      <path class="wave-band" d="M0 232 C 120 298, 300 292, 430 255 C 550 225, 640 222, 700 240 L700 400 L0 400 Z"/>
    </svg>

    <div class="contact">
      <p class="person-name">Marek TL Olvani</p>
      <p class="person-title">President</p>
      <p class="contact-line">
        <span>marek.olvani.consulting@mailbox.example</span>
        <svg class="contact-icon" viewBox="0 0 18 18" aria-hidden="true">
          <rect x="1.5" y="4" width="15" height="10" rx="1"/>
          <path d="M1.5 4.5 L9 10 L16.5 4.5"/>
        </svg>
      </p>
      <p class="contact-line">
        <span>www.marekolvaniconsulting.example</span>
        <svg class="contact-icon" viewBox="0 0 18 18" aria-hidden="true">
          <circle cx="9" cy="9" r="7.5"/>
          <ellipse cx="9" cy="9" rx="3.2" ry="7.5"/>
          <path d="M1.5 9 H16.5 M3 5 H15 M3 13 H15"/>
        </svg>
      </p>
    </div>
  </section>

</main>
</body>
</html>
```